HML5 Web Application Design

We need a graphic design to give a HTML web application a modern look and feel. The design should be clean and neat with a metro inspired interface. All application uses vormanta controls so any experience with these would be great.
Perhaps you could also include a few screenshots of your previous work

Industry/Entity Type

Graphic Design

Requirements
Must have
• Must be HTML 5 compliant

```html
<!DOCTYPE html>
<html lang="en">
<head>
<meta charset="utf-8">
<title>Supplier Transactions</title>
<link href="https://fonts.googleapis.com/css2?family=Arimo:wght@400;700&display=swap" rel="stylesheet">
<style>
  :root {
    --brand-blue: #0099d8;
    --bar-dark: #424242;
    --text-dark: #3c3c3c;
    --text-body: #333333;
    --row-alt: #f4f4f4;
    --row-plain: #ffffff;
    --rule: #dcdcdc;
    --pager-bg: #ececec;
    --input-border: #d6d6d6;
    --white: #ffffff;
  }
  * { box-sizing: border-box; margin: 0; padding: 0; }
  html, body { width: 1200px; height: 633px; overflow: hidden; }
  body {
    position: relative;
    background: var(--white);
    font-family: "Arimo", Arial, sans-serif;
    color: var(--text-body);
  }
  .site-header { position: absolute; left: 0; top: 0; width: 1200px; height: 59px; }
  .brand {
    position: absolute; left: 23px; top: 11px;
    font-size: 32px; font-weight: 700; letter-spacing: -0.5px;
    color: var(--text-dark);
  }
  .user-name { position: absolute; left: 1048px; top: 8px; font-size: 11px; color: var(--text-dark); }
  .log-off { position: absolute; left: 1135px; top: 7px; font-size: 11px; font-weight: 700; color: var(--brand-blue); text-decoration: none; }

  .main-nav { position: absolute; left: 0; top: 59px; width: 1200px; height: 31px; background: var(--bar-dark); }
  .main-nav a {
    position: absolute; top: 0; height: 31px; line-height: 31px;
    font-size: 11px; color: var(--white); text-decoration: none;
  }
  .main-nav a.is-active { background: var(--brand-blue); width: 71px; text-align: center; left: 0; }

  .page-title {
    position: absolute; left: 20px; top: 131px;
    font-size: 28px; font-weight: 400; color: var(--text-dark);
  }
  .title-rule { position: absolute; left: 18px; top: 170px; width: 1164px; height: 1px; background: var(--rule); }

  .date-filter { position: absolute; left: 0; top: 190px; height: 28px; width: 1200px; }
  .date-filter label { position: absolute; top: 6px; font-size: 13px; color: var(--text-dark); letter-spacing: 0.3px; }
  .date-input {
    position: absolute; top: 1px; width: 125px; height: 26px;
    border: 1px solid var(--input-border); padding-left: 15px;
    font-family: inherit; font-size: 11px; color: var(--text-body); line-height: 24px;
  }
  .calendar-icon { position: absolute; top: 8px; width: 13px; height: 13px; }

  .transactions { position: absolute; left: 18px; top: 228px; width: 1158px; border: 1px solid var(--rule); }
  .transactions table { width: 100%; border-collapse: collapse; table-layout: fixed; }
  .transactions th {
    background: var(--brand-blue); color: var(--white);
    height: 28px; font-size: 11px; font-weight: 700; text-align: left;
    padding-left: 26px; position: relative; border-left: 1px solid var(--white);
  }
  .transactions th:first-child { border-left: none; }
  .sort-arrow { position: absolute; right: 11px; top: 11px; width: 7px; height: 5px; }
  .transactions td {
    height: 24.7px; font-size: 10.5px; padding-left: 29px;
    border-left: 1px solid var(--rule); color: var(--text-body);
  }
  .transactions td:first-child { border-left: none; padding-left: 24px; }
  .transactions tbody tr:nth-child(odd) td { background: var(--row-alt); }
  .transactions tbody tr:nth-child(even) td { background: var(--row-plain); }

  .pager { position: relative; height: 30px; background: var(--pager-bg); border-top: 1px solid var(--rule); }
  .pager-btn { position: absolute; top: 6px; width: 19px; height: 19px; background: var(--brand-blue); }
  .pager-btn svg { position: absolute; left: 5px; top: 5px; }
  .page-numbers { position: absolute; left: 66px; top: 11px; font-size: 10.5px; word-spacing: 1px; color: var(--text-body); }
  .pager-info { position: absolute; right: 14px; top: 10px; font-size: 10.5px; color: var(--text-body); }
  .pager-info em { font-style: normal; color: var(--brand-blue); }

  .site-footer {
    position: absolute; left: 0; top: 600px; width: 1200px; height: 33px;
    background: var(--bar-dark); border-top: 2px solid var(--brand-blue);
  }
  .site-footer p { position: absolute; left: 19px; top: 10px; font-size: 11px; color: var(--white); }
</style>
</head>
<body>
  <header class="site-header">
    <div class="brand">Vormanta</div>
    <span class="user-name">Daniel Reeve</span>
    <a class="log-off" href="#">Log off</a>
  </header>

  <nav class="main-nav">
    <a class="is-active" href="#">Home</a>
    <a href="#" style="left:105px">Pin Rquests</a>
    <a href="#" style="left:202px">Transactions</a>
    <a href="#" style="left:303px">Tax Details</a>
    <a href="#" style="left:400px">Users</a>
    <a href="#" style="left:472px">Suppliers</a>
    <a href="#" style="left:568px">Queries</a>
    <a href="#" style="left:647px">LA Staff Queries</a>
  </nav>

  <h1 class="page-title">Supplier Transactions Screen</h1>
  <div class="title-rule"></div>

  <div class="date-filter">
    <label style="left:21px">Date From:</label>
    <div class="date-input" style="left:102px">01/01/2013</div>
    <svg class="calendar-icon" style="left:234px" viewBox="0 0 13 13">
      <rect x="0.5" y="1.5" width="12" height="11" fill="none" stroke="#777"/>
      <rect x="0.5" y="1.5" width="12" height="2.5" fill="#777"/>
      <g fill="#777"><rect x="2.5" y="6" width="2" height="1.5"/><rect x="5.5" y="6" width="2" height="1.5"/><rect x="8.5" y="6" width="2" height="1.5"/><rect x="2.5" y="9" width="2" height="1.5"/><rect x="5.5" y="9" width="2" height="1.5"/><rect x="8.5" y="9" width="2" height="1.5"/></g>
    </svg>
    <label style="left:264px">Date To:</label>
    <div class="date-input" style="left:330px">01/08/2013</div>
    <svg class="calendar-icon" style="left:462px" viewBox="0 0 13 13">
      <rect x="0.5" y="1.5" width="12" height="11" fill="none" stroke="#777"/>
      <rect x="0.5" y="1.5" width="12" height="2.5" fill="#777"/>
      <g fill="#777"><rect x="2.5" y="6" width="2" height="1.5"/><rect x="5.5" y="6" width="2" height="1.5"/><rect x="8.5" y="6" width="2" height="1.5"/><rect x="2.5" y="9" width="2" height="1.5"/><rect x="5.5" y="9" width="2" height="1.5"/><rect x="8.5" y="9" width="2" height="1.5"/></g>
    </svg>
  </div>

  <section class="transactions">
    <table>
      <thead>
        <tr>
          <th>Date<svg class="sort-arrow" viewBox="0 0 7 5"><path d="M0 0h7L3.5 5z" fill="#fff"/></svg></th>
          <th>Type<svg class="sort-arrow" viewBox="0 0 7 5"><path d="M0 0h7L3.5 5z" fill="#fff"/></svg></th>
          <th>Reference<svg class="sort-arrow" viewBox="0 0 7 5"><path d="M0 0h7L3.5 5z" fill="#fff"/></svg></th>
          <th>Amount<svg class="sort-arrow" viewBox="0 0 7 5"><path d="M0 0h7L3.5 5z" fill="#fff"/></svg></th>
          <th>Status<svg class="sort-arrow" viewBox="0 0 7 5"><path d="M0 0h7L3.5 5z" fill="#fff"/></svg></th>
        </tr>
      </thead>
      <tbody>
        <tr><td>01/01/2000</td><td>Inv</td><td>9999</td><td>100</td><td>Received</td></tr>
        <tr><td>01/01/2000</td><td>Payment</td><td>99999</td><td>80</td><td>Payment</td></tr>
        <tr><td>01/01/2000</td><td>Inv</td><td>9999</td><td>100</td><td>Received</td></tr>
        <tr><td>01/01/2000</td><td>Payment</td><td>999</td><td>80</td><td>Payment</td></tr>
        <tr><td>01/01/2000</td><td>Inv</td><td>45454</td><td>100</td><td>Received</td></tr>
        <tr><td>01/01/2000</td><td>Payment</td><td>3636</td><td>80</td><td>Payment</td></tr>
        <tr><td>01/01/2000</td><td>Inv</td><td>4554</td><td>100</td><td>Received</td></tr>
        <tr><td>01/01/2000</td><td>Payment</td><td>108</td><td>80</td><td>Payment</td></tr>
        <tr><td>01/01/2000</td><td>Inv</td><td>99</td><td>100</td><td>Received</td></tr>
        <tr><td>01/01/2000</td><td>Payment</td><td>99999999</td><td>80</td><td>Payment</td></tr>
      </tbody>
    </table>
    <div class="pager">
      <span class="pager-btn" style="left:13px"><svg width="9" height="9" viewBox="0 0 9 9"><rect x="0.5" y="0.5" width="1.5" height="8" fill="#fff"/><path d="M8 0.5v8L3 4.5z" fill="#fff"/></svg></span>
      <span class="pager-btn" style="left:39px"><svg width="9" height="9" viewBox="0 0 9 9"><path d="M7 0.5v8L2 4.5z" fill="#fff"/></svg></span>
      <span class="page-numbers">1 2 3 4 5 6 7 8 9</span>
      <span class="pager-btn" style="left:171px"><svg width="9" height="9" viewBox="0 0 9 9"><path d="M2 0.5v8L7 4.5z" fill="#fff"/></svg></span>
      <span class="pager-btn" style="left:198px"><svg width="9" height="9" viewBox="0 0 9 9"><path d="M1 0.5v8L6 4.5z" fill="#fff"/><rect x="7" y="0.5" width="1.5" height="8" fill="#fff"/></svg></span>
      <span class="pager-info">Page <em>1</em> of <em>10</em>, items <em>1</em> to <em>7</em> of <em>90</em>.</span>
    </div>
  </section>

  <footer class="site-footer">
    <p>© 2013 Norvale.&nbsp; All Rights Reserved</p>
  </footer>
</body>
</html>
```